Improve design on www.vorntakvagt.dk.

The company provides securitysolutions, primarily guards, doorguards, eventsecurity and night club.

Target Market(s)

Private and business, who needs security.

Industry/Entity Type

Club

Requirements
Must have
• Don't use inline style.
Menus must use UL/LI tags.
Nice to have
• Nice animation maybe, shiny.

```html
<!DOCTYPE html>
<html lang="da">
<head>
<meta charset="utf-8">
<title>Vagtnet – Om os</title>
<link href="https://fonts.googleapis.com/css2?family=Arimo:wght@400;700&family=Bebas+Neue&family=Gelasio:ital@1&display=swap" rel="stylesheet">
<style>
:root{
  --ink:#222;
  --muted:#444;
  --brand:#9b2b1e;
  --link-red:#d61414;
  --frame:#3a3336;
  --field:#d3d3d3;
  --field-edge:#b9b9b9;
  --tab:#e6e6e6;
  --footer:#d9d9d9;
  --white:#fff;
}
*{box-sizing:border-box;margin:0;padding:0}
html,body{width:1200px;height:1200px;overflow:hidden;background:var(--white)}
body{position:relative;font-family:"Arimo",Arial,sans-serif;color:var(--ink)}
ul{list-style:none}
a{color:inherit;text-decoration:none}

.brand{position:absolute;left:125px;top:52px;display:flex;align-items:center;gap:10px}
.brand-mark{width:52px;height:52px;background:var(--brand)}
.brand-name{font-family:"Arimo",Arial,sans-serif;font-weight:700;font-size:34px;color:var(--ink);letter-spacing:-1px}

.util-nav{position:absolute;right:94px;top:38px;display:flex;gap:8px;font-size:12px;color:var(--muted)}

.main-nav{position:absolute;left:395px;top:94px;display:flex}
.main-nav li{height:31px;padding:7px 9px 0;font-size:15px;color:#111}
.main-nav li.is-active{background:var(--tab);border:1px solid #c9c9c9;border-bottom:none;border-radius:4px 4px 0 0;padding:6px 12px 0}

.hero{position:absolute;left:121px;top:125px;width:992px;height:377px;border:5px solid var(--frame);border-radius:9px;overflow:hidden}
.hero-photo{position:absolute;inset:0;background:linear-gradient(100deg,#4e4e4e 0%,#8a8a8a 30%,#3a3a3a 55%,#9a9a9a 80%,#cfcfcf 100%)}
.hero-title{position:absolute;left:26px;top:236px;font-family:"Bebas Neue",Impact,sans-serif;font-size:58px;line-height:55px;color:var(--white);letter-spacing:1px}

.crumb{position:absolute;left:129px;top:510px;font-family:"Gelasio",Georgia,serif;font-style:italic;font-size:12px;color:var(--muted)}

.about{position:absolute;left:131px;top:551px;width:670px}
.section-title{font-family:"Gelasio",Georgia,serif;font-style:italic;font-weight:400;font-size:19px;line-height:24px;letter-spacing:1px;color:#333}
.about p,.quote p{font-size:12.5px;line-height:14.3px;color:var(--ink)}
.about .intro{margin:34px 0 0 4px}
.about .intro a{color:var(--link-red)}
.about-brand{display:flex;align-items:center;gap:8px;margin:25px 0 0 4px;height:56px}
.about-brand .brand-mark{width:56px;height:56px;background:#555}
.about-brand .brand-name{font-size:34px;color:#333}
.about-body{margin:38px 0 0 4px}
.about-body p+p{margin-top:14.3px}

.quote{position:absolute;left:843px;top:527px;width:260px}
.quote .section-title{margin-left:3px}
.quote .lead{margin-top:18px}
.quote .note{margin-top:14.3px}
.quote-form{margin-top:26px;margin-left:9px;width:224px}
.quote-form label{display:block;font-size:12.5px;margin:0 0 7px 3px}
.quote-form .field{display:block;width:223px;height:26px;background:var(--field);border:1px solid var(--field-edge);border-radius:5px;margin-bottom:12px;box-shadow:inset 0 2px 3px rgba(0,0,0,.12)}
.quote-form .field-area{height:106px}
.form-actions{display:flex;justify-content:flex-end;gap:28px;margin-top:16px;font-size:12.5px;padding-right:3px}

.site-footer{position:absolute;left:0;top:1166px;width:1200px;height:34px;background:var(--footer);font-size:11px;color:#333}
.footer-nav{position:absolute;left:140px;top:11px;display:flex;gap:15px}
.copyright{position:absolute;right:115px;top:11px}
</style>
</head>
<body>
<header>
  <div class="brand"><span class="brand-mark"></span><span class="brand-name">VAGTNET</span></div>
  <ul class="util-nav"><li><a href="#">faq</a></li><li>|</li><li><a href="#">login</a></li></ul>
  <nav>
    <ul class="main-nav">
      <li class="is-active"><a href="#">Om os</a></li>
      <li><a href="#">Vagtydelser</a></li>
      <li><a href="#">Kontakt</a></li>
      <li><a href="#">Afdelinger</a></li>
      <li><a href="#">Login Ansatte</a></li>
      <li><a href="#">Login Ledere</a></li>
      <li><a href="#">Jobs</a></li>
      <li><a href="#">Franchisetager</a></li>
    </ul>
  </nav>
</header>

<section class="hero">
  <div class="hero-photo" role="img" aria-label="Black and white photo of a security guard on duty outside a busy nightlife venue"></div>
  <h1 class="hero-title">YOUR SECURITY<br>IS OUR JOB</h1>
</section>

<p class="crumb">» Om os</p>

<main class="about">
  <h2 class="section-title">Know about our company,<br>Virksomhedsprofil:</h2>
  <p class="intro">Vagtnet er et netværk af lokale vagt- og dørmandsvirksomheder i Danmark. Selskabet bag netværket ejer selv nogle afdelinger, imens resten fungerer som franchise-afdelinger, 100 % ejet af personerne bag afdelingen. Har du interesse i at få dit eget vagt- og/eller dørmandsfirma i Vagtnet ? <a href="#">Så klik her...</a></p>
  <div class="about-brand"><span class="brand-mark"></span><span class="brand-name">VAGTNET</span></div>
  <div class="about-body">
    <p>Vagtnet adskiller sig fra andre vagtvirksomheder, ved vores fleksibilitet, serviceniveau og loyalitet overfor gældende lovgivning.</p>
    <p>Hver afdeling har sin egen side her på sitet. Denne finder du under fanebladet "Afdelinger". Her kan du læse om afdelingen, hvad der tilbydes, og finde kontaktinformation.</p>
    <p>Du kan også kontakte os direkte ved at bruge formularen i venstre side - din henvendelse vil så blive videresendt til den relevante afdeling.</p>
    <p>Vagtnet blev grundlagt i foråret 2006. Vort mål var dengang at levere professionelle dørmands- og sikkerhedsvagtløsninger. Vi har siden starten mærket stigende efterspørgsel på vores ydelser, og er nu førende indenfor dette, flere steder i landet.</p>
    <p>De ledende kræfter i Vagtnet, har til sammen over 20 års erfaring i branchen, både i ind- og udland.</p>
    <p>Vagtnet er et firma hvor god holdning og moral, er en selvfølge.<br>Vi arbejder altid på at give kunden den bedst mulige service, vi tror på det gode samarbejde, og hos os er kunden altid i fokus.</p>
    <p>Vagtnet tilbyder vore kunder, præcist det de efterspørger, vi skræddersyr hver enkelt opgave, stor som lille så den passer perfekt til dig og dit sted.<br>vi specialuddanner gerne folk, så du bedre kan udnytte deres tid, hos dig.</p>
  </div>
</main>

<aside class="quote">
  <h2 class="section-title">Få et tilbud eller en<br>Dørmand / Vagt på prøve</h2>
  <p class="lead">Udfyldelse af denne formular giver dig mulighed for at indhente et tilbud på en ydelse, eller evt. få en vagt gratis på prøve. Din henvendelse vil blive videresendt til den afdeling som er nærmest dig.</p>
  <p class="note">(ikke til forespørgsler om ansættelse: vil du søge ansættelse, skal du istedet kontakte den relevante afdeling direkte pr. mail, post eller telefon)</p>
  <form class="quote-form">
    <label>Navn</label><span class="field"></span>
    <label>Email</label><span class="field"></span>
    <label>Telefon</label><span class="field"></span>
    <label>Vedr.</label><span class="field field-area"></span>
    <div class="form-actions"><span>send</span><span>reset</span></div>
  </form>
</aside>

<footer class="site-footer">
  <ul class="footer-nav"><li>Kontakt</li><li>Login Ansatte</li><li>Login Ledere</li><li>Jobs</li></ul>
  <p class="copyright">© 2011 Vagtnet ApS.&nbsp; Tlf: 4120 3300. All rights reserved.</p>
</footer>
</body>
</html>
```